Q.R. Bright Desk Store

The design is for eCommerce home page but I would like it to complement this site: http://www.qrbrightdesksystems.com/ but... it should also have independence as a standalone site.

The best design will be able to effectively mix corporate with a high quality small business consumer feel. It should be completely custom design, not a template look or feel. I want the users to get the feeling that this is the place to go for buying tech for business. We sell the same products as Vantrel.

You can be creative as you wish, as long as the elements of a great eCommerce site are present.

I would like your 'design' to blow these away:
http://www.buying.zorvex.com/
mivoland.com
http://www.vantrel.com/

Here are references:
Call to action
http://trabelwise.com/us/blog/48173-seven-tips-for-designing-an-effective-ecommerce-call-to-action

Effective Ecommerce design
http://www.plov.com/ss/7-tips-for-effective-e-commerce#0

91 points of ecommerce
http://dreb.com/blog/holygrail-of-ecommerce-conversion-optimization-91-points-checklist

UPDATE 07/11/2013:

Please look at the category sample png files. I see already many people are using the main menu from qrbrightdesksystems.com and I do not mind your creativiety, but this is an eCommerce store and people need a menu to get to the categories and/or product types. I don't want to limit anyone creativity by the png samples. I'm also not using them to show I like them in any particular way or form, just that it's needed, whether it's a button (dropdown of course) that says 'Categories' or 'Products, whether it an accordion, horizontal or vertical.

Thanks

UPDATE 07/12/2013:

Please find other use of space that has been used for About Us paragraph (if you've added it to the page). About Us should have it's own page and the purpose of the design should be to sell products (and some services as products). Please put a link or some other creative method to lead users to the About Us page.

Reason: I've raised the award, including 1st, 2nd, and 3rd place and participation payments so I will also extend 7 days. Thanks!

I've updated the product brief. Please scroll down to where it says: UPDATE 07/11/2013

Thanks!

UPDATE 07/12/2013:

Please find other use of space that has been used for About Us paragraph (if you've added it to the page).  About Us should have it's own page and the purpose of the design should be to sell products (and some services as products). Please put a link or some other creative method to lead users to the About Us page if you must but not on the real estate of the page.

Thanks!

Added updates to the brief 7/14/2013.

Thanks!

The voting is in and the project is complete.  Thanks everyone for joining, all of those who participated are truly amazingly talented. But, there were only 3 prizes.  I will be having further projects down the line to develop other pages to this site after the initial implementation is completed.  I truly would like to have you all back. 

- Thank you.

Target Market(s)

corporate decision-makers AND small business consumers

Industry/Entity Type

Small Business

Requirements
Must have
• Call to action.
Openness (non-clutter).

These elements:
Search box
Logo
Tagline
Telephone number
Contact details
Address
My account / sign in
Shopping basket / checkout link
Latest offers
Promotional area
Email sign up
Delivery information
About us
Link to press office / corporate site
Terms and conditions
Sitemap for the footer.
Delivery offers: free
Personalized recommendations
Social media links
Accepted payment methods
Link to blog or community section
Change language / country

http://freshnotesblog.kelvarant.com/sales-leads-landing-page/

UPDATE 07/14/2013
Category Menu. This can be a dropdown, horizontal, vertical, etc. But shoppers need to know how to get to the products they want to buy.
Nice to have
• Trustmarks
Blog/Blog link

UPDATE 07/12/2013:
Make the footer useful.

UPDATE 07/14/2013 (Suggestions of elements to differentiate your designs)

-Quick Shop: A quick buy module/section: Where a user can put in a SKU number or Model number to quickly add the product to their shopping cart.

-Featured
-Best Sellers
-Specials
-Trending Tags/Tag Cloud
- Activity Stream
- Cross Sell/ Up Sell
- Testimonial
- Social Network Feed
- Live Help
- Feedback/Support/Contact Tab
- Show logged in user (i.e. Welcome, Mark Pell)
Should not have
• The design SHOULD NOT be generic like this:

http://www.artflock.com/design/52392
http://www.pelicanvault.com/

The page should not feel over cluttered. It should not have low quality icons or design elements. Navigation should not be hard to discover or confusing.

```html
<!DOCTYPE html>
<html lang="en">
<head>
<meta charset="utf-8">
<title>Q.R. Bright Desk Store</title>
<link href="https://fonts.googleapis.com/css2?family=Arimo:wght@400;700&display=swap" rel="stylesheet">
<style>
:root{
  --blue:#1b5da6;--link:#2b7fcb;--dark:#2f2f2f;--text:#555;--line:#d9d9d9;
  --navtop:#f4f4f4;--navbot:#d8d8d8;--foot:#363636;--band:#474747;--panel:#ececec;--green:#3aa635;
}
*{box-sizing:border-box;margin:0;padding:0}
html,body{width:742px;height:1200px;overflow:hidden;background:#fff}
body{position:relative;font-family:Arimo,Arial,sans-serif;color:var(--text);font-size:8px}
.a{position:absolute}
a{color:inherit;text-decoration:none}
.topline{left:0;top:0;width:742px;height:20px;border-bottom:1px solid #eee}
.toplinks{left:88px;top:6px;color:var(--link);font-size:8px;word-spacing:1px}
.userlinks{left:482px;top:5px;color:#333;font-size:7.5px}
.logo{left:86px;top:28px;display:flex;align-items:center;gap:5px}
.logo .dot{width:36px;height:36px;border-radius:50%;background:var(--blue)}
.logo span{font-size:17px;color:var(--blue);font-weight:700;line-height:1}
.offer{left:230px;top:29px;font-size:7.5px;color:#333}
.offer b{color:var(--link);font-weight:400}
.search{left:230px;top:46px;width:202px;height:20px;border:1px solid #ccc;border-radius:2px;padding:5px 8px;font-style:italic;color:#888;font-size:7.5px}
.go{left:432px;top:45px;width:30px;height:22px;background:var(--blue);color:#fff;font-weight:700;font-size:9px;text-align:center;line-height:22px;border-radius:0 3px 3px 0}
.sel{top:25px;height:14px;border:1px solid #ccc;font-size:7.5px;color:#333;padding:2px 5px;font-weight:700}
.flag{left:636px;top:27px;width:16px;height:11px;background:#2c4a8f}
.call{left:527px;top:55px;font-size:11px;color:#222;font-weight:700;display:flex;align-items:center;gap:3px}
.call span{color:var(--blue);font-weight:400}
.nav{left:0;top:76px;width:742px;height:26px;background:linear-gradient(var(--navtop),var(--navbot));border-top:1px solid #ccc;border-bottom:1px solid #bbb}
.nav a{position:absolute;top:9px;font-size:7.5px;color:#333;letter-spacing:.4px}
.cattab{left:207px;top:76px;width:75px;height:22px;background:var(--link);color:#fff;font-size:7.5px;padding:9px 0 0 16px;letter-spacing:.4px}
.drop{left:207px;top:98px;width:106px;background:rgba(38,131,206,.95)}
.drop div{height:17.4px;border-bottom:1px solid rgba(255,255,255,.25);color:#fff;font-size:7.5px;font-weight:700;padding:5px 0 0 6px;letter-spacing:.3px}
.livehelp{left:517px;top:85px;color:var(--green);font-weight:700;font-size:7.5px}
.cart{left:579px;top:78px;width:75px;height:23px;background:var(--blue);border-radius:3px;color:#fff;font-size:8.5px;padding:6px 0 0 26px}
.hero{left:88px;top:110px;width:566px;height:200px;border:1px solid #ccc;border-bottom:2px solid #bbb}
.heroimg{left:96px;top:112px;width:232px;height:196px;background:linear-gradient(135deg,#3a3a3a,#8ab2d6 60%,#eef3f7)}
.badge{left:332px;top:114px;width:80px;height:80px;border-radius:50%;background:#3aa3d9;color:#fff;font-weight:700;font-size:15px;text-align:center;padding-top:24px;line-height:14px}
.herotxt{left:446px;top:134px;color:#222;font-size:8px}
.herotxt h2{color:var(--blue);font-size:18px;margin:10px 0 12px}
.herotxt li{list-style:none;font-size:7.5px;margin-bottom:7px;padding-left:9px;position:relative}
.herotxt li:before{content:"";position:absolute;left:0;top:2px;border-left:4px solid #999;border-top:3px solid transparent;border-bottom:3px solid transparent}
.btn{background:var(--blue);color:#fff;font-weight:700;font-size:7px;display:flex;align-items:center;gap:5px;padding:0 6px}
.btn i{width:10px;height:10px;border-radius:50%;background:#fff;display:inline-block;position:relative}
.btn i:after{content:"";position:absolute;left:4px;top:2.5px;border-left:3px solid var(--blue);border-top:2.5px solid transparent;border-bottom:2.5px solid transparent}
.promo{top:323px;width:160px;height:141px;border:1px solid #ccc}
.promo .bar{position:absolute;left:0;bottom:0;width:100%;height:23px;background:#111;color:#fff;font-weight:700;font-size:8px;padding:7px 6px}
.promo .bar b{position:absolute;right:6px;top:7px;font-size:9px}
.ph{position:absolute}
.tabs{left:88px;top:475px;width:566px;height:27px;background:linear-gradient(#eee,#d6d6d6)}
.tabblue{left:88px;top:475px;width:134px;height:27px;background:var(--link);color:#fff;font-size:12px;padding:7px 0 0 8px}
.panel{left:88px;top:502px;width:566px;height:218px;background:var(--panel)}
.feat{left:88px;top:502px;width:146px;height:218px;background:#fff}
.card{width:191px;height:96px;background:#fff;border:1px solid #ddd}
.card h4,.feat h4{color:var(--blue);font-size:9px;position:absolute}
.card p,.feat p{position:absolute;font-size:6.8px;line-height:10.5px;color:#555}
.price{position:absolute;font-size:8px;font-weight:700;color:#555}
.price span{color:var(--link)}
.atc{position:absolute;height:14px}
.det{position:absolute;height:14px;width:42px;background:#ddd;border:1px solid #bbb;font-size:6.5px;font-weight:700;color:#333;text-align:center;line-height:12px}
.social{left:94px;top:730px;width:177px;height:180px;border:1px solid #ccc}
.stabs{position:absolute;left:0;top:0;width:100%;height:20px;background:var(--blue);color:#fff;font-size:9px}
.h3{font-size:11px;color:#333;font-weight:700}
.quote{left:282px;top:762px;width:177px;height:100px;background:#f0f0f0;border-radius:3px;padding:9px 10px;font-size:7.5px;line-height:12px;font-style:italic;color:#666;text-align:right}
.blog{left:479px;width:176px;height:40px}
.blog .th{position:absolute;left:0;top:2px;width:40px;height:34px;background:linear-gradient(#bfd9ef,#5d8fc2)}
.blog p{position:absolute;left:47px;top:0;font-size:7px;line-height:10.5px;color:#666}
.blog p b{color:var(--blue);font-weight:400}
.news{left:0;top:932px;width:742px;height:36px;background:var(--band)}
.foot{left:0;top:968px;width:742px;height:232px;background:var(--foot);color:#bbb}
.col{position:absolute;top:12px}
.col h5{font-size:9.5px;color:#fff;font-weight:400;margin-bottom:8px;width:100px}
.col div{font-size:7px;height:22px;border-top:1px solid #555;padding-top:6px;width:80px}
.col div:first-of-type{border-top:1px solid #555}
.circ{width:14px;height:14px;border-radius:50%;background:#555;display:inline-block;margin-right:4px}
</style>
</head>
<body>
<div class="a topline"></div>
<div class="a toplinks">Home &nbsp;| &nbsp;Small Business &nbsp;| &nbsp;Enterprise &nbsp;| &nbsp;Non-Profit</div>
<div class="a userlinks">Welcome &nbsp;| &nbsp;Login &nbsp;| &nbsp;My Account &nbsp;| &nbsp;Checkout</div>

<div class="a logo"><div class="dot"></div><span>Q.R. BRIGHT<br>DESK</span></div>
<div class="a offer">Additionl 25% Off on orders above $ 19.99 | <b>8 Hours Only</b></div>
<div class="a search">Search for items</div>
<div class="a go">GO</div>
<div class="a sel" style="left:482px;width:83px">Currency : &nbsp;CHF ▾</div>
<div class="a sel" style="left:574px;width:58px;border:none">Language : ▾</div>
<div class="a flag"></div>
<div class="a call"><svg width="12" height="12" viewBox="0 0 12 12"><path d="M2 1l2 0 1 3-1.5 1a6 6 0 003 3L7.5 6.5l3 1 0 2c0 1-1 1.5-2 1.5A8.5 8.5 0 011 3c0-1 .5-2 1-2z" fill="#1b5da6"/></svg>Call Us:<span>123 123 1234</span></div>

<nav class="a nav">
  <a style="left:98px">Home</a><a style="left:155px">About Us</a>
  <a style="left:299px">Featured</a><a style="left:367px">Our Services</a><a style="left:451px">Contact Us</a>
</nav>
<div class="a cattab">Categories</div>
<div class="a drop">
  <div>» Desktops</div><div>» Laptops &amp; Notebooks</div><div>&nbsp; Components</div><div>» Tablets</div>
  <div>» Software</div><div>» Phones &amp; PDAs</div><div>» Cameras</div><div>» MP3 Players</div>
</div>
<div class="a livehelp">Live Help</div>
<div class="a cart">My Cart (0)</div>
<svg class="a" style="left:586px;top:82px" width="16" height="14" viewBox="0 0 16 14"><path d="M0 1h3l2 8h8l2-6H4" fill="none" stroke="#fff" stroke-width="1.5"/><circle cx="6" cy="12" r="1.3" fill="#fff"/><circle cx="12" cy="12" r="1.3" fill="#fff"/></svg>

<div class="a hero"></div>
<div class="a heroimg" role="img" aria-label="Tablet and smartphone showing app icons"></div>
<div class="a badge">TODAY<br>ONLY</div>
<div class="a herotxt">
  <p>Choose from the latest variety of</p>
  <h2>MOBILE PHONE</h2>
  <ul><li>Lorem ipsum dolor sit amet, consectetur &nbsp;elit.</li><li>Consectetur adipiscing elit X23</li><li>Mauris quis lacinia diam Z12</li><li>Tortor porta velit faucibus 22" x 212</li></ul>
</div>
<a class="a btn" style="left:444px;top:258px;height:18px">SHOP NOW <i></i></a>

<section class="a promo" style="left:106px">
  <div class="ph" style="left:6px;top:8px;color:var(--blue);font-size:13.5px;font-weight:700">50% off On</div>
  <div class="ph" style="left:4px;top:26px;color:#333;font-size:11.5px">Selected Items</div>
  <p class="ph" style="left:5px;top:49px;width:80px;font-size:6.8px;line-height:10.5px">Lorem ipsum sit amet, consectetur adipiscing elit. Mauris quis lacinia diam.</p>
  <div class="ph" role="img" aria-label="Smartphone with app icons" style="left:85px;top:12px;width:70px;height:104px;background:linear-gradient(#222,#6b7f95)"></div>
  <div class="bar">TABLETS <b>SHOP NOW »</b></div>
</section>
<section class="a promo" style="left:291px">
  <div class="ph" style="left:9px;top:11px;color:var(--blue);font-size:16px;font-weight:700;line-height:21px">DEALS<br>OF THE WEEk</div>
  <div class="ph" style="left:12px;top:58px;font-size:7.5px;color:#444">Easy EMI for 3 / 6 / 9 / 12 Months</div>
  <div class="ph" style="left:12px;top:78px;font-size:8px;color:var(--link);line-height:14px">UP TO<br>59% OFF</div>
  <div class="bar">FREE SHIPPING <b>SHOP NOW »</b></div>
</section>
<section class="a promo" style="left:478px">
  <div class="ph" style="left:11px;top:9px;font-size:15px;font-weight:700;color:#333"><span style="color:var(--blue)">Free!</span> Delivery</div>
  <div class="ph" role="img" aria-label="Free shipping illustration with parcel" style="left:6px;top:40px;width:90px;height:62px;background:linear-gradient(#f3d49a,#e3e3e3);border-radius:6px"></div>
  <p class="ph" style="left:94px;top:40px;width:64px;font-size:6.8px;line-height:10.5px">Lorem ipsum sit amet, consectetur adipiscing elit. Mauris quis lacinia diam.</p>
  <div class="bar"><b>SHOP NOW »</b></div>
</section>

<div class="a tabs"></div>
<div class="a tabblue">Top Featured Products</div>
<div class="a" style="left:230px;top:482px;font-size:12px;color:#222">Best Sellers</div>
<div class="a" style="left:608px;top:486px;font-size:7px;color:#333">View All ●</div>
<div class="a panel"></div>
<div class="a feat">
  <h4 style="left:14px;top:11px">Lorem ipsum dolor sit</h4>
  <div class="ph" role="img" aria-label="Security software box" style="left:33px;top:30px;width:62px;height:100px;background:linear-gradient(135deg,#c62b1b,#f0a020)"></div>
  <p style="left:15px;top:136px;width:115px">Enjoy high-quality viewing and easy connectivity at a price within</p>
  <div class="price" style="left:15px;top:172px">Price: <span>$255</span></div>
  <a class="btn atc" style="left:14px;top:193px">Add To Cart <i></i></a>
  <div class="det" style="left:83px;top:193px">Details »</div>
</div>

<div class="a card" style="left:246px;top:510px">
  <div class="ph" role="img" aria-label="Software box" style="left:10px;top:12px;width:56px;height:72px;background:linear-gradient(135deg,#0c5fa8,#7cc3ea)"></div>
  <h4 style="left:74px;top:8px">Lorem ipsum dolor sit</h4>
  <p style="left:74px;top:26px;width:110px">Enjoy high-quality viewing and easy connectivity at a price within</p>
  <div class="price" style="left:74px;top:61px">Price: <span>$255</span></div>
  <a class="btn atc" style="left:74px;top:77px">Add To Cart <i></i></a><div class="det" style="left:141px;top:77px">Details »</div>
</div>
<div class="a card" style="left:450px;top:510px">
  <div class="ph" role="img" aria-label="Smartphone with app icons" style="left:10px;top:12px;width:56px;height:72px;background:linear-gradient(#222,#7890a8)"></div>
  <h4 style="left:74px;top:8px">Lorem ipsum dolor sit</h4>
  <p style="left:74px;top:26px;width:110px">Enjoy high-quality viewing and easy connectivity at a price within</p>
  <div class="price" style="left:74px;top:61px">Price: <span>$255</span></div>
  <a class="btn atc" style="left:74px;top:77px">Add To Cart <i></i></a><div class="det" style="left:141px;top:77px">Details »</div>
</div>
<div class="a card" style="left:246px;top:615px">
  <div class="ph" role="img" aria-label="Desktop printer" style="left:6px;top:16px;width:62px;height:62px;background:linear-gradient(#f2f2f2,#a9a9a9)"></div>
  <h4 style="left:74px;top:8px">Lorem ipsum dolor sit</h4>
  <p style="left:74px;top:26px;width:110px">Enjoy high-quality viewing and easy connectivity at a price within</p>
  <div class="price" style="left:74px;top:61px">Price: <span>$255</span></div>
  <a class="btn atc" style="left:74px;top:77px">Add To Cart <i></i></a><div class="det" style="left:141px;top:77px">Details »</div>
</div>
<div class="a card" style="left:450px;top:615px">
  <div class="ph" role="img" aria-label="Security software box" style="left:10px;top:12px;width:50px;height:72px;background:linear-gradient(135deg,#c62b1b,#f0a020)"></div>
  <h4 style="left:74px;top:8px">Lorem ipsum dolor sit</h4>
  <p style="left:74px;top:26px;width:110px">Enjoy high-quality viewing and easy connectivity at a price within</p>
  <div class="price" style="left:74px;top:61px">Price: <span>$255</span></div>
  <a class="btn atc" style="left:74px;top:77px">Add To Cart <i></i></a><div class="det" style="left:141px;top:77px">Details »</div>
</div>

<section class="a social">
  <div class="stabs"><span style="position:absolute;left:5px;top:3px;background:#fff;color:var(--blue);padding:2px 3px;height:17px">Friendlist</span><span style="position:absolute;left:62px;top:6px">Chirpline</span></div>
  <div class="ph" style="left:10px;top:28px;width:20px;height:20px;border-radius:50%;background:var(--blue)"></div>
  <div class="ph" style="left:50px;top:33px;font-size:5.5px;color:#555"><span style="border:1px solid #aab;padding:1px 3px;color:var(--blue)">Like</span> 108 people like Brightdesk</div>
  <div class="ph" role="img" aria-label="Grid of follower profile pictures" style="left:8px;top:56px;width:160px;height:104px;background:repeating-linear-gradient(90deg,#c9a58a 0 30px,#fff 30px 34px)"></div>
  <div class="ph" style="left:8px;top:168px;font-size:5.5px;color:#666">■ Friendlist social plugin</div>
</section>
<div class="a h3" style="left:283px;top:737px">What Clients Say?</div>
<div class="a" style="left:282px;top:756px;width:177px;border-top:1px solid var(--line)"></div>
<div class="a quote">Lorem ipsum dolor sit amet, consectetuer adipiscing elit, sed diam nonummy nibh euismod tincidunt ut laoreet dolore magna aliquam erat volutpat. &nbsp;Lorem ipsum dolor sit amet, consectetuer adipiscing elit, sed diam nonummy nibh euismod tincidunt ut laoreet dolore magna aliquam erat volutpat.</div>
<div class="a" style="left:324px;top:868px;font-size:7.5px;color:#444;font-weight:700">- Euismod tincidunt</div>

<div class="a h3" style="left:479px;top:737px">Latest Blog</div>
<div class="a" style="left:479px;top:756px;width:176px;border-top:1px solid var(--line)"></div>
<div class="a blog" style="top:766px"><div class="th" role="img" aria-label="Laptop and monitor"></div><p><b>Lorem ipsum</b> sit amet, consectetur adipi scing elit. Mauris quis lacinia.<br><b>12 june 2013</b></p></div>
<div class="a blog" style="top:812px"><div class="th" role="img" aria-label="Laptop and monitor"></div><p><b>Lorem ipsum</b> sit amet, consectetur adipi scing elit. Mauris quis lacinia.<br><b>12 june 2013</b></p></div>
<div class="a blog" style="top:858px"><div class="th" role="img" aria-label="Laptop and monitor"></div><p><b>Lorem ipsum</b> sit amet, consectetur adipi scing elit. Mauris quis lacinia .<br><b>12 june 2013</b></p></div>
<a class="a" style="left:602px;top:896px;width:53px;height:17px;background:var(--blue);color:#fff;font-size:7.5px;font-weight:700;text-align:center;line-height:17px">Read more»</a>

<div class="a news">
  <svg class="a" style="left:90px;top:10px" width="24" height="16" viewBox="0 0 24 16"><rect x="1" y="1" width="22" height="14" fill="none" stroke="#bbb" stroke-width="1.5"/><path d="M1 1l11 8 11-8M1 15l8-7M23 15l-8-7" fill="none" stroke="#bbb" stroke-width="1.2"/></svg>
  <div class="a" style="left:124px;top:8px;color:#fff;font-weight:700;font-size:8px;line-height:13px">Don't want to miss exciting offers!!<br>Sign up for our newsletters</div>
  <div class="a" style="left:281px;top:8px;width:142px;height:19px;background:#fff;font-style:italic;font-size:7.5px;color:#777;padding:5px 5px">Enter your email here</div>
  <div class="a" style="left:427px;top:8px;width:44px;height:19px;background:var(--blue);color:#fff;font-size:7.5px;font-weight:700;text-align:center;line-height:19px">Submit</div>
  <div class="a" style="left:518px;top:12px;color:#fff;font-size:9.5px">Follow Us on</div>
  <div class="a" style="left:582px;top:11px"><span class="circ"></span><span class="circ"></span><span class="circ"></span><span class="circ"></span></div>
</div>

<footer class="a foot">
  <div class="col" style="left:87px"><h5>Our Company</h5><div>About Us</div><div>Careers</div><div>Corporate</div><div>Partners</div></div>
  <div class="col" style="left:198px"><h5>Main Menu</h5><div>Home</div><div>Small Business</div><div>Enterprise</div><div>Non-Profit</div></div>
  <div class="col" style="left:321px"><h5>User Menu</h5><div>Go Shopping</div><div>Billing</div><div>Get Support</div><div>Contact Us</div></div>
  <div class="col" style="left:442px"><h5>Our Websites</h5><div style="width:84px">qrbrightstore.com</div><div style="width:84px">qrbrightinc.com</div><div style="width:84px">qrbrightsupport.com</div><div style="width:84px">qrbrighteducation.com</div></div>
  <div class="col" style="left:566px"><h5>Product and Services</h5><div>Hardwarew Fulfillment</div><div>Software Licensing</div><div>Resource Management</div><div>Technical Services</div></div>
  <div class="col" style="left:87px;top:134px"><h5>Programs</h5><div>Exchange Board</div><div>Partner Program</div><div>Recycle</div></div>
  <div class="col" style="left:200px;top:134px"><h5>New York</h5>
    <div style="width:124px;height:38px;line-height:11px;padding-left:18px;border:none;position:relative"><svg style="position:absolute;left:2px;top:5px" width="7" height="10" viewBox="0 0 7 10"><path d="M3.5 0A3.5 3.5 0 000 3.5C0 6 3.5 10 3.5 10S7 6 7 3.5A3.5 3.5 0 003.5 0z" fill="#ccc"/></svg>47 Alder Lane, Suite #120<br>Greyford, NY 10542</div>
    <div style="width:124px;padding-left:18px;position:relative;border:none"><svg style="position:absolute;left:0;top:5px" width="11" height="8" viewBox="0 0 11 8"><rect width="11" height="8" fill="#ccc"/><path d="M0 0l5.5 4L11 0" fill="none" stroke="#363636"/></svg>+1 (888) XXX XXXX</div>
    <div style="width:124px;padding-left:18px;position:relative;border:none"><svg style="position:absolute;left:1px;top:5px" width="9" height="9" viewBox="0 0 12 12"><path d="M2 1l2 0 1 3-1.5 1a6 6 0 003 3L7.5 6.5l3 1 0 2c0 1-1 1.5-2 1.5A8.5 8.5 0 011 3c0-1 .5-2 1-2z" fill="#ccc"/></svg>info@qrbrightinc.com</div>
  </div>
  <div class="a" style="left:350px;top:136px;color:#fff;font-size:9.5px;font-weight:700">Payment Mode :</div>
  <div class="a" style="left:350px;top:153px;display:flex;gap:4px">
    <span style="width:26px;height:13px;background:#6d8fc4"></span><span style="width:26px;height:13px;background:#fff"></span><span style="width:26px;height:13px;background:#e9a03a"></span><span style="width:26px;height:13px;background:#f2f2f2"></span><span style="width:26px;height:13px;background:#f4e98c"></span>
  </div>
  <div class="a" style="left:350px;top:180px;width:58px;height:34px;background:#fff;border-radius:2px"></div>
  <div class="a" style="left:546px;top:144px;display:flex;align-items:center;gap:5px"><span style="width:30px;height:30px;border-radius:50%;background:#666"></span><span style="font-size:14px;color:#ddd;font-weight:700;line-height:1">Q.R. BRIGHT<br>DESK</span></div>
  <div class="a" style="left:543px;top:189px;font-size:7px;color:#bbb">Copyright 2013 it on brightdesk</div>
  <div class="a" style="left:562px;top:200px;font-size:7.5px;color:#ddd;font-weight:700">Terms and Conditions</div>
</footer>
</body>
</html>
```